For Lease sign for Property management company in Kansas City

We need someone to take our information and design a standard for lease sign that we can put in front of each of our buildings. I would love for it to do its job of letting people know there are units available but also be unique somehow. Also the aspect ratio of the design would ideally be 4 wide by 3 tall but we open to other ideas. It will be a larger yard sign.

Target Market(s)

Potential Tenants

Industry/Entity Type

Real Estate Development

Font styles to use
Sans Serif

Requirements
Must have
• Our logo, our website (www.quillstead-properties.com), our phone number (816) 555-2719.
Nice to have
• Some how say "For Lease"
Sign to be 4' wide by 3' tall
If there was a place to put the building name that would be cool but not ne
Should not have
• Nothing that I can think of

```html
<!DOCTYPE html>
<html lang="en">
<head>
<meta charset="utf-8">
<title>Quillstead Properties – For Lease Yard Sign</title>
<link rel="stylesheet" href="https://fonts.googleapis.com/css2?family=Barlow:wght@600;700;800&display=swap">
<style>
  :root {
    --backdrop: #d1d2d4;
    --charcoal: #58585a;
    --lease-orange: #f9ae40;
    --brand-red: #bf1f2b;
    --paper: #ffffff;
    --mist-top: #f1f2f6;
    --mist-bottom: #dcdfea;
    --ink-grey: #545456;
  }
  html, body {
    margin: 0;
    padding: 0;
    width: 1200px;
    height: 1000px;
    overflow: hidden;
    background: var(--backdrop);
  }
  .canvas {
    position: relative;
    width: 1200px;
    height: 1000px;
  }
  .lease-sign {
    position: absolute;
    left: 40px;
    top: 81px;
    width: 1120px;
    height: 839px;
    display: block;
    box-shadow: 0 2px 6px rgba(0,0,0,0.25);
  }
  .headline {
    font-family: "Barlow", sans-serif;
    font-weight: 800;
    fill: var(--lease-orange);
  }
  .website {
    font-family: "Barlow", sans-serif;
    font-weight: 700;
    fill: var(--paper);
  }
  .brand-name {
    font-family: "Barlow", sans-serif;
    font-weight: 700;
    fill: var(--brand-red);
  }
  .phone {
    font-family: "Barlow", sans-serif;
    font-weight: 700;
    fill: var(--ink-grey);
  }
  .top-panel { fill: var(--charcoal); }
  .red-band { fill: var(--brand-red); }
  .logo-band { fill: var(--paper); }
  .brand-mark { fill: var(--lease-orange); }
</style>
</head>
<body>
<main class="canvas">
  <svg class="lease-sign" viewBox="0 0 1218 912" xmlns="http://www.w3.org/2000/svg" aria-label="For lease sign">
    <defs>
      <linearGradient id="top-sheen" x1="0" y1="0" x2="0" y2="1">
        <stop offset="0" stop-color="#58585a"/>
        <stop offset="0.55" stop-color="#5a5a5c"/>
        <stop offset="1" stop-color="#6a6b6e"/>
      </linearGradient>
      <linearGradient id="bottom-mist" x1="0" y1="0" x2="0" y2="1">
        <stop offset="0" stop-color="var(--mist-top)"/>
        <stop offset="1" stop-color="var(--mist-bottom)"/>
      </linearGradient>
    </defs>

    <!-- top panel -->
    <rect class="top-panel" x="0" y="0" width="1218" height="367" fill="url(#top-sheen)"/>

    <!-- bottom contact panel -->
    <rect x="0" y="674" width="1218" height="238" fill="url(#bottom-mist)"/>

    <!-- white logo band -->
    <rect class="logo-band" x="0" y="392" width="1218" height="258"/>

    <!-- red bands with angled tabs -->
    <polygon class="red-band" points="0,367 1069,367 1139,292 1218,292 1218,392 0,392"/>
    <polygon class="red-band" points="0,650 1218,650 1218,747 1139,747 1069,674 0,674"/>

    <!-- headline -->
    <text class="headline" x="99" y="247" font-size="206" textLength="1021" lengthAdjust="spacingAndGlyphs">FOR LEASE</text>

    <!-- website -->
    <text class="website" x="609" y="324" font-size="60" text-anchor="middle" textLength="880" lengthAdjust="spacingAndGlyphs">WWW.QUILLSTEAD-PROPERTIES.COM</text>

    <!-- brand lockup -->
    <circle class="brand-mark" cx="262" cy="519" r="155"/>
    <text class="brand-name" x="460" y="535" font-size="118" textLength="652" lengthAdjust="spacingAndGlyphs">QUILLSTEAD</text>
    <text class="brand-name" x="460" y="624" font-size="82" textLength="652" lengthAdjust="spacingAndGlyphs">PROPERTIES</text>

    <!-- phone -->
    <text class="phone" x="94" y="842" font-size="150" textLength="956" lengthAdjust="spacingAndGlyphs">(816) 555-2719</text>
  </svg>
</main>
</body>
</html>
```